business card for a massage therapy practice named 'Meadow and Willow Massage Studio'

I really need a trendy, yet easy on the eyes business card to complement my logo. Ideally with some gold or rose gold foil work.

My uploaded file of the logo I have in horizontal but I have a vertical version as well. Another color that is used in the website is a blush pink here and there. I'd like to see some trendy tropical leaves in the design.

```html
<!DOCTYPE html>
<html lang="en">
<head>
<meta charset="utf-8">
<title>Meadow &amp; Willow Massage Studio — Business Card</title>
<link href="https://fonts.googleapis.com/css2?family=Work+Sans:wght@400;500&family=Satisfy&display=swap" rel="stylesheet">
<style>
  :root {
    --stage: #232324;
    --card: #1a1a1b;
    --card-edge: #b39a6b;
    --gold: #b7a27a;
    --ink: #f4f2ee;
    --rule: #e9e6e0;
  }
  * { box-sizing: border-box; margin: 0; padding: 0; }
  html, body { width: 1200px; height: 900px; overflow: hidden; }
  body {
    background: var(--stage);
    font-family: "Work Sans", Arial, sans-serif;
    display: flex;
    flex-direction: column;
    align-items: center;
    justify-content: center;
    gap: 40px;
  }
  .card {
    width: 700px;
    height: 400px;
    background: var(--card);
    border-bottom: 4px solid var(--card-edge);
    position: relative;
    display: flex;
    align-items: center;
  }
  .brand {
    display: flex;
    align-items: center;
    gap: 16px;
  }
  .brand-dot {
    width: 40px;
    height: 40px;
    border-radius: 50%;
    background: var(--gold);
    flex: none;
  }
  .brand-name {
    color: var(--ink);
    font-weight: 500;
    font-size: 30px;
    line-height: 1.15;
    letter-spacing: 0.5px;
  }
  .card-front { justify-content: center; }
  .card-back { padding-left: 70px; }
  .card-back .brand-name { font-size: 24px; }
  .divider {
    width: 2px;
    height: 170px;
    background: var(--rule);
    margin: 0 34px 0 36px;
  }
  .contact { color: var(--ink); }
  .person-name {
    font-family: "Satisfy", cursive;
    color: var(--gold);
    font-size: 30px;
    margin-bottom: 12px;
  }
  .address {
    font-size: 15px;
    line-height: 1.4;
    margin-bottom: 12px;
  }
  .contact-line {
    display: flex;
    align-items: center;
    gap: 10px;
    font-size: 15px;
    line-height: 1.55;
  }
  .contact-line svg { width: 12px; height: 12px; flex: none; }
</style>
</head>
<body>
  <section class="card card-front" aria-label="Card front">
    <div class="brand">
      <span class="brand-dot"></span>
      <span class="brand-name">Meadow &amp; Willow<br>Massage Studio</span>
    </div>
  </section>

  <section class="card card-back" aria-label="Card back">
    <div class="brand">
      <span class="brand-dot"></span>
      <span class="brand-name">Meadow &amp; Willow<br>Massage Studio</span>
    </div>
    <span class="divider"></span>
    <div class="contact">
      <p class="person-name">Marisol Vega</p>
      <p class="address">2240 Alder Ln. suite 112,<br>Fairview, CA 95000</p>
      <p class="contact-line">
        <svg viewBox="0 0 12 12" aria-hidden="true"><path d="M3 1 L5 3.5 L4 5 C5 7 6 8 7.5 8.5 L9 7.5 L11 9.5 L9.5 11 C5 10.5 1.5 7 1 2.5 Z" fill="var(--gold)"/></svg>
        (555) 214-7730
      </p>
      <p class="contact-line">
        <svg viewBox="0 0 12 12" aria-hidden="true"><rect x="1" y="2.5" width="10" height="7" fill="none" stroke="var(--gold)" stroke-width="1.2"/><path d="M1 2.5 L6 6.5 L11 2.5" fill="none" stroke="var(--gold)" stroke-width="1.2"/></svg>
        meadowandwillow@mail.com
      </p>
      <p class="contact-line">
        <svg viewBox="0 0 12 12" aria-hidden="true"><circle cx="6" cy="6" r="5" fill="none" stroke="var(--gold)" stroke-width="1.2"/><ellipse cx="6" cy="6" rx="2.2" ry="5" fill="none" stroke="var(--gold)" stroke-width="1"/><path d="M1 6 H11" stroke="var(--gold)" stroke-width="1"/></svg>
        www.meadowandwillow.com
      </p>
    </div>
  </section>
</body>
</html>
```